Business Card Design

our business is purchasing, rehabbing and flipping homes. Design a house in the palm of a hand. This card is for a new company based in Georgia. So we buy homes that have been foreclosed, short sales,abandond, old homes and vacant homes.
We help improve the communities that we work in. We would like to see designs that use a black background with green accent and other colors that blend and don't take away from the logo and other important information.

Industry/Entity Type

Business

Contact Information for Business Card

Mavenbrook Holdings
Turning Old Doors Into New Starts
2738 Fenwick Lane
Duluth GA 30418
Office: 678-555-0192
mavenbrookholdingsllc.example

```html
<!DOCTYPE html>
<html lang="en">
<head>
<meta charset="utf-8">
<title>Mavenbrook Holdings – Business Card</title>
<link rel="stylesheet" href="https://fonts.googleapis.com/css2?family=Fjalla+One&family=Roboto:wght@300;400&display=swap">
<style>
  :root {
    --page-bg: #ececec;
    --card-dark: #2b2b2b;
    --brand-green: #56ab0c;
    --text-light: #ffffff;
  }
  * { margin: 0; padding: 0; box-sizing: border-box; }
  html, body {
    width: 1200px;
    height: 804px;
    overflow: hidden;
    background: var(--page-bg);
  }
  .card {
    position: absolute;
    left: 88px;
    top: 101px;
    width: 1008px;
    height: 581px;
    border-radius: 54px;
    overflow: hidden;
    background: var(--card-dark);
    box-shadow: 0 4px 14px rgba(0,0,0,0.18);
  }
  .card__wave {
    position: absolute;
    left: 0;
    top: 0;
    width: 1008px;
    height: 581px;
  }
  .contact {
    position: absolute;
    left: 82px;
    color: var(--text-light);
    font-family: "Roboto", sans-serif;
    font-weight: 300;
    font-size: 30px;
    display: flex;
    align-items: center;
    gap: 14px;
    letter-spacing: 0.2px;
  }
  .contact svg { flex: none; }
  .contact--phone { top: 113px; }
  .contact--web { top: 166px; }
  .contact--address { top: 258px; }
  .brand {
    position: absolute;
    left: 630px;
    top: 48px;
    width: 260px;
    display: flex;
    flex-direction: column;
    align-items: center;
    gap: 22px;
  }
  .brand__mark {
    width: 150px;
    height: 150px;
    border-radius: 50%;
    background: var(--brand-green);
  }
  .brand__name {
    font-family: "Fjalla One", sans-serif;
    font-size: 30px;
    color: var(--text-light);
    white-space: nowrap;
  }
  .tagline {
    position: absolute;
    left: 0;
    width: 100%;
    top: 436px;
    text-align: center;
    font-family: "Fjalla One", sans-serif;
    font-size: 64px;
    line-height: 1;
    color: var(--text-light);
  }
</style>
</head>
<body>
  <div class="card">
    <svg class="card__wave" viewBox="0 0 1008 581" aria-hidden="true">
      <path d="M0 372 Q 480 318 1008 380 L1008 581 L0 581 Z" fill="var(--brand-green)"/>
      <path d="M0 366 Q 480 312 1008 374" fill="none" stroke="var(--text-light)" stroke-width="7"/>
    </svg>

    <div class="contact contact--phone">
      <svg width="28" height="30" viewBox="0 0 24 24" aria-hidden="true">
        <path fill="#fff" d="M6.6 2.5c.5-.3 1.1-.2 1.4.3l2 3.2c.3.5.2 1.1-.2 1.4L8.4 8.5c.8 2.6 3.2 5.6 5.8 7l1.3-1.3c.4-.4 1-.4 1.4-.1l3.1 2.1c.5.3.6 1 .3 1.4l-1.2 1.9c-.5.8-1.5 1.2-2.4 1-5.6-1.4-10.4-6.6-11.6-12.3-.2-.9.2-1.8 1-2.3z"/>
      </svg>
      <span>678-555-0192</span>
    </div>

    <div class="contact contact--web">
      <svg width="30" height="30" viewBox="0 0 24 24" aria-hidden="true">
        <g fill="none" stroke="#fff" stroke-width="1.5">
          <circle cx="12" cy="12" r="10"/>
          <ellipse cx="12" cy="12" rx="4.5" ry="10"/>
          <line x1="2" y1="12" x2="22" y2="12"/>
          <path d="M4 7h16M4 17h16"/>
        </g>
      </svg>
      <span>mavenbrookholdingsllc.example</span>
    </div>

    <div class="contact contact--address">
      <svg width="28" height="44" viewBox="0 0 24 36" aria-hidden="true">
        <path fill="#fff" d="M12 0C5.4 0 0 5.2 0 11.7 0 20 12 36 12 36s12-16 12-24.3C24 5.2 18.6 0 12 0zm0 16.5a5 5 0 1 1 0-10 5 5 0 0 1 0 10z"/>
      </svg>
      <span>2738 Fenwick Lane Duluth GA 30418</span>
    </div>

    <div class="brand">
      <div class="brand__mark"></div>
      <div class="brand__name">Mavenbrook Holdings</div>
    </div>

    <div class="tagline">Turning Old Doors Into New Starts</div>
  </div>
</body>
</html>
```